Website Update for Global Company - Solar Technology - Brisqell

We recently released our first version of our website kelvaris.com. However despite a longer process of developing the page, it is still missing the elements of a brilliant website. (Currently it looks dead and boring) We are having problems integrating our logo and want to create a more catching site. The task involves an updated and without changing most of main elements in the existing page. (Unless you can do it even better) The blue color needs to be kept but can be changed within the blue-spectrum. The logo text (KELVARIS) must be better integrated in the site, however the main logo could be used in elements like we have tried with the background. The surface of the logo could be changed to 3D or metallic, or any other theme that would make the site more complete.
It would be good if some elements of the site could be used on business cards and invoices to keep the company identity.
Kelvaris is a new development company specialized in green energy and sustainable development. We do design, engineering, manufacturing, sourcing and other processes related to product development – both as consultants and for own products.
Keep the look of the site as professional as possible, and with a cooperate-looking style.

Link to existing page: www.kelvaris.com

Brief Update : After reviewing the designs we would like all new and current designers to make more bold designs that stands out from the rest. We do not like the standard layout that looks like any other cooperate homepage. We want a very unique and very lively page - with faded images and effects when hoovering like seen on our existing page. Try make all elements blend together, and use faded background images instead of just white color - or something else.

Make the site unique !

Industry/Entity Type

Solar Energy

Contact Information for Business Card

Owner/Founder/CEO : Frederik Lysgaard Holm
Company name: Kelvaris ApS
Email: frederik.lysgaard@kelvaris.dk
Phone: +45 71 83 96 54
Slogan Sustainable Development
Address: Havnestien 18, 2
DK-5820 Svendborg, Denmark

Number of Pages Required

3 page

Font styles to use
Serif
Sans Serif

Colors
0555a3
85acd3
cedeed
3176b5
cee9f5
85cae6
0293ce
86cfc6
33b8a4

```html
<!DOCTYPE html>
<html lang="en">
<head>
<meta charset="utf-8">
<title>Kelvaris — Sustainable Development</title>
<link href="https://fonts.googleapis.com/css2?family=Open+Sans:wght@400;600;700;800&display=swap" rel="stylesheet">
<style>
  :root{
    --blue:#0293ce;
    --blue-deep:#0555a3;
    --blue-mid:#3176b5;
    --blue-soft:#85cae6;
    --ink:#1d2430;
    --gray:#e9ecef;
    --white:#ffffff;
  }
  *{box-sizing:border-box;margin:0;padding:0}
  html,body{width:1200px;height:2300px;overflow:hidden;background:#f1f3f5}
  body{font-family:"Open Sans",Arial,sans-serif;color:var(--ink);position:relative}

  .site-header{position:absolute;left:0;top:0;width:1200px;height:56px;background:var(--white);display:flex;align-items:center;justify-content:space-between;padding:0 40px 0 28px}
  .brand{display:flex;align-items:center;gap:10px}
  .brand-mark{width:22px;height:22px;background:var(--blue)}
  .brand-name{font-weight:800;font-size:24px;letter-spacing:1px;color:var(--ink)}
  .main-nav{display:flex;gap:44px}
  .main-nav a{font-size:11px;font-weight:600;color:#55606c;text-decoration:none;letter-spacing:.5px}
  .main-nav a.active{color:var(--blue)}

  .hero{position:absolute;left:0;top:56px;width:1200px;height:504px;
    background:linear-gradient(180deg,#2c7fc4 0%,#8cc2ea 38%,#b9c3c7 58%,#6f6457 78%,#3d342c 100%)}
  .hero-panels{position:absolute;left:0;top:110px;width:720px;height:394px;
    background:linear-gradient(160deg,#1b2a44 0%,#24406a 50%,#0f1b2d 100%);clip-path:polygon(0 0,70% 20%,100% 100%,0 100%)}
  .hero-copy{position:absolute;right:40px;top:250px;text-align:right;color:var(--white)}
  .hero-copy h1{font-size:44px;font-weight:800;line-height:44px;letter-spacing:4px;text-transform:uppercase}
  .hero-copy p{font-size:13px;margin-top:10px;opacity:.92}

  .tile{position:absolute;height:228px;overflow:hidden}
  .photo{background:linear-gradient(135deg,#04152a 0%,#0a3d75 55%,#0b72c4 100%)}
  .photo.alt{background:linear-gradient(200deg,#02101f 0%,#08335f 50%,#1681d0 100%)}
  .photo.bright{background:linear-gradient(120deg,#0a4e95 0%,#1e8fd6 60%,#0a3463 100%)}
  .photo.dark{background:radial-gradient(circle at 50% 50%,#0d3f72 0%,#05182c 70%,#020a14 100%)}
  .solid{background:var(--blue);color:var(--white);display:flex;align-items:center;justify-content:center;text-align:center;padding:0 30px;font-weight:700;font-size:21px;line-height:28px}
  .tile-icon{position:absolute;left:50%;top:50%;transform:translate(-50%,-50%);width:74px;height:74px;fill:none;stroke:#fff;stroke-width:3;stroke-linecap:round;stroke-linejoin:round}

  .news{background:var(--white);display:flex;align-items:center;padding:0 30px;gap:30px}
  .news-title{color:var(--blue);font-weight:800;font-size:22px;line-height:24px;border-left:3px solid var(--blue);padding-left:12px;width:110px}
  .news-list{list-style:none;display:flex;flex-direction:column;gap:22px}
  .news-list li{display:flex;gap:14px;align-items:flex-start}
  .news-dot{width:20px;height:20px;border:2px solid var(--blue);border-radius:3px;flex:none;margin-top:3px}
  .news-list h3{font-size:15px;font-weight:600;color:var(--ink)}
  .news-list p{font-size:11px;color:#7a8591}

  .problem{background:var(--white);display:flex;align-items:center;padding:0 46px;gap:26px}
  .problem h2{color:var(--blue);font-size:22px;font-weight:700;line-height:28px}

  .site-footer{position:absolute;left:0;top:2080px;width:1200px;height:220px;background:var(--gray)}
  .footer-cols{position:absolute;left:80px;top:22px;display:flex;gap:56px}
  .footer-cols h4{color:var(--blue);font-size:14px;font-weight:800;margin-bottom:6px}
  .footer-cols li{list-style:none;font-size:11px;line-height:16px;color:#3a4550;text-transform:uppercase}
  .footer-right{position:absolute;right:80px;top:22px;text-align:right}
  .social{display:flex;gap:8px;justify-content:flex-end}
  .social span{width:22px;height:22px;border-radius:50%;background:var(--blue-mid)}
  .phone{color:var(--blue);font-size:34px;font-weight:800;margin-top:8px;letter-spacing:1px}
  .footer-brand{display:flex;align-items:center;gap:12px;justify-content:flex-end;margin-top:6px}
  .footer-brand .brand-mark{width:34px;height:34px}
  .footer-brand .brand-name{font-size:46px;letter-spacing:2px}
  .copyright{position:absolute;left:80px;bottom:16px;font-size:12px;font-weight:600;color:var(--blue)}
</style>
</head>
<body>
  <svg width="0" height="0" style="position:absolute" aria-hidden="true">
    <defs>
      <symbol id="i-gear" viewBox="0 0 74 74">
        <circle cx="37" cy="37" r="11"/>
        <path d="M37 14v8M37 52v8M14 37h8M52 37h8M21 21l6 6M47 47l6 6M53 21l-6 6M27 47l-6 6"/>
        <circle cx="37" cy="37" r="19"/>
      </symbol>
      <symbol id="i-play" viewBox="0 0 74 74">
        <circle cx="37" cy="37" r="34"/>
        <polygon points="30,23 52,37 30,51" fill="#fff" stroke="none"/>
      </symbol>
      <symbol id="i-case" viewBox="0 0 74 74">
        <rect x="12" y="26" width="50" height="34" rx="3"/>
        <path d="M28 26v-7h18v7M12 40h50"/>
      </symbol>
      <symbol id="i-bulb" viewBox="0 0 74 74">
        <path d="M27 44c-5-4-8-9-8-15a18 18 0 0 1 36 0c0 6-3 11-8 15v6H27z"/>
        <path d="M29 56h16M31 62h12M37 4v4M12 14l3 3M62 14l-3 3"/>
      </symbol>
      <symbol id="i-pencil" viewBox="0 0 74 74">
        <path d="M16 58l4-14 30-30 10 10-30 30z"/>
        <path d="M44 20l10 10M10 64h54"/>
      </symbol>
      <symbol id="i-flask" viewBox="0 0 74 74">
        <path d="M29 10h16M32 10v20L16 58c-2 4 0 6 4 6h34c4 0 6-2 4-6L42 30V10"/>
        <path d="M22 48h30"/>
      </symbol>
      <symbol id="i-chip" viewBox="0 0 74 74">
        <rect x="20" y="20" width="34" height="34" rx="3"/>
        <rect x="29" y="29" width="16" height="16"/>
        <path d="M28 20v-8M37 20v-8M46 20v-8M28 54v8M37 54v8M46 54v8M20 28h-8M20 37h-8M20 46h-8M54 28h8M54 37h8M54 46h8"/>
      </symbol>
      <symbol id="i-arm" viewBox="0 0 74 74">
        <path d="M14 62h28M22 62v-8h12v8M28 54L38 30l18 -8"/>
        <circle cx="38" cy="30" r="4"/>
        <path d="M56 22l6 -6M56 22l6 4"/>
      </symbol>
      <symbol id="i-tools" viewBox="0 0 74 74">
        <path d="M16 58l26-26M48 12a10 10 0 0 0-8 14l4 4a10 10 0 0 0 14-8l-6 2-4-4z"/>
        <path d="M58 58L30 30M24 14l10 10-6 6-10-10z"/>
      </symbol>
    </defs>
  </svg>

  <header class="site-header">
    <div class="brand"><span class="brand-mark"></span><span class="brand-name">KELVARIS</span></div>
    <nav class="main-nav">
      <a class="active" href="#">HOME</a><a href="#">EXPERTISE</a><a href="#">APPROACH</a><a href="#">CLIENT</a><a href="#">ABOUT</a><a href="#">CONTACT</a>
    </nav>
  </header>

  <section class="hero" role="img" aria-label="Solar panel field beneath mountains and a blue sky">
    <div class="hero-panels"></div>
    <div class="hero-copy">
      <h1>Design<br>Engineering<br>Source<br>Manufacturing</h1>
      <p>We provide complete services throughout the product development process</p>
    </div>
  </section>

  <div class="tile news" style="left:80px;top:572px;width:510px">
    <div class="news-title">IN<br>THE<br>NEWS</div>
    <ul class="news-list">
      <li><span class="news-dot"></span><div><h3>Launch of website</h3><p>Read the latest update</p></div></li>
      <li><span class="news-dot"></span><div><h3>First project initiated</h3><p>Read the latest update</p></div></li>
      <li><span class="news-dot"></span><div><h3>Establishment of Kelvaris ApS</h3><p>Read the latest update</p></div></li>
    </ul>
  </div>
  <div class="tile photo dark" style="left:610px;top:572px;width:510px" role="img" aria-label="Hand touching a glowing digital interface in blue tones">
    <svg class="tile-icon"><use href="#i-gear"/></svg>
  </div>

  <div class="tile photo bright" style="left:80px;top:824px;width:510px" role="img" aria-label="Engineer working in a laboratory, blue toned">
    <svg class="tile-icon"><use href="#i-case"/></svg>
  </div>
  <div class="tile photo alt" style="left:610px;top:824px;width:510px" role="img" aria-label="Wall of screens showing engineering work, blue toned">
    <svg class="tile-icon"><use href="#i-play"/></svg>
  </div>

  <div class="tile solid" style="left:80px;top:1076px;width:333px">Kelvaris Is Made Up Of Talented + Divers Individuals</div>
  <div class="tile photo dark" style="left:433px;top:1076px;width:333px" role="img" aria-label="Glowing light bulb idea scene">
    <svg class="tile-icon"><use href="#i-bulb"/></svg>
  </div>
  <div class="tile photo" style="left:786px;top:1076px;width:334px" role="img" aria-label="Engineering design sketch on a desk">
    <svg class="tile-icon"><use href="#i-pencil"/></svg>
  </div>

  <div class="tile solid" style="left:80px;top:1328px;width:333px">Maker Space</div>
  <div class="tile photo bright" style="left:433px;top:1328px;width:333px" role="img" aria-label="Circuit board close-up">
    <svg class="tile-icon"><use href="#i-gear"/></svg>
  </div>
  <div class="tile photo alt" style="left:786px;top:1328px;width:334px" role="img" aria-label="Research lab equipment">
    <svg class="tile-icon"><use href="#i-flask"/></svg>
  </div>

  <div class="tile photo dark" style="left:80px;top:1580px;width:510px" role="img" aria-label="Glowing microchip on a circuit board">
    <svg class="tile-icon"><use href="#i-chip"/></svg>
  </div>
  <div class="tile problem" style="left:610px;top:1580px;width:510px">
    <svg width="70" height="70" viewBox="0 0 70 70" aria-hidden="true"><circle cx="35" cy="35" r="32" fill="none" stroke="#0293ce" stroke-width="4"/><polyline points="21,36 31,46 50,25" fill="none" stroke="#0293ce" stroke-width="5" stroke-linecap="round" stroke-linejoin="round"/></svg>
    <h2>We Are Looking For<br>New Problem To Solve</h2>
  </div>

  <div class="tile photo bright" style="left:80px;top:1832px;width:510px" role="img" aria-label="Robotic arms on a manufacturing line">
    <svg class="tile-icon"><use href="#i-arm"/></svg>
  </div>
  <div class="tile photo alt" style="left:610px;top:1832px;width:510px" role="img" aria-label="Control room screens, blue toned">
    <svg class="tile-icon"><use href="#i-tools"/></svg>
  </div>

  <footer class="site-footer">
    <div class="footer-cols">
      <div><h4>QUICK LINKS</h4><ul><li>Home</li><li>Work</li><li>Expertise</li><li>Approach</li><li>Client</li><li>About</li><li>Contact</li></ul></div>
      <div><h4>EXPERTISE</h4><ul><li>Design</li><li>Engineering</li><li>Source</li><li>Prototyping</li><li>Manufacturing</li><li>Innovations</li></ul></div>
      <div><h4>ABOUT</h4><ul><li>History</li><li>Career</li><li>Team</li></ul></div>
    </div>
    <div class="footer-right">
      <div class="social"><span></span><span></span><span></span><span></span><span></span><span></span></div>
      <div class="phone">+45 71 83 96 54</div>
      <div class="footer-brand"><span class="brand-mark"></span><span class="brand-name">KELVARIS</span></div>
    </div>
    <div class="copyright">Copyright©2015 Kelvaris. All Rights Reserved.</div>
  </footer>
</body>
</html>
```